Childrens Business Card Design Project

We have an existing logo attached which we'd like to use as part of our new business card design.

The design needs to be relatively gender neutral and contain bright colours.

In terms of look and feel think:

Fun, Modern, Quality (as opposed to cheap!) and of course Party!

Single or double sided - i am not decided on either one yet - ideally i'd like to see designs for both because if you think stylistically it would benefit having two sides then please try it out!

I think the challenge here is finding a really good background colour (if you think it needs one) and also choosing an eye grabbing text that compliments the existing logo - do that an you are onto a winner! I have another image for the business (which i have attached) which uses stripes so i am keen to see a design that incorporates this to tie in all my collateral.

The copy required is as follows (not necesarily in this order)

Bookings/Enquiries:

Tilda

T: 0498 217 503
E: enquiries@brightfoxparties.example.au

ABN: 47 302 658 114

Any feedback on text is welcomed - please message me or add to the discussion.

Reason: Hi All, I have received some promising designs, but overall i am not impressed with the quality of the work so have extended the deadline as this project has been committed. I will aim to attach some business card examples to the brief tomorrow to give further guidance as a whole but please do not submit any designs on a generic background that are not related to the theme, have been carelessly placed with overlapping elements - it just looks sloppy. For those who have read the brief an incorporated stripes or even spots this is on target as it convey's a party theme, however please work on getting the colours for the contact details by either a bold solid strip to highlight or some other way to frame it. When it comes to the logo, some people have removed the characters all together and changed the colour of the wording - this is fine. Also feel free to balloons starts - but keep it classy and watch your placement of these. I hope this helps and for the designs i would like to see revisions for i will aim to get back to you individually over the next day or so. Many thanks all.

Target Market(s)

Mothers in the suburbs of Australia with a disposal able income, children aged between 1-7 years old.

Industry/Entity Type

Business

Requirements
Must have
• The font and wording positioning must compliment the logo.

```html
<!DOCTYPE html>
<html lang="en">
<head>
<meta charset="utf-8">
<title>Bright Fox – Business Card</title>
<link href="https://fonts.googleapis.com/css2?family=Comic+Neue:wght@400;700&display=swap" rel="stylesheet">
<style>
  :root {
    --page: #efece6;
    --sky-top: #b9dff5;
    --sky-bottom: #f1f9fd;
    --bubble: #4fcdf1;
    --name-red: #e3262c;
    --phone-blue: #1d5cb4;
    --email-white: #ffffff;
    --abn-yellow: #ffe640;
    --brand-blue: #2a9fdf;
    --tagline-gold: #e9b82c;
    --art-warm: #f6c9b4;
    --art-cool: #a9d8f1;
  }
  * { margin: 0; padding: 0; box-sizing: border-box; }
  html, body {
    width: 1200px; height: 675px; overflow: hidden;
    background: var(--page);
    font-family: "Comic Neue", "Comic Sans MS", cursive;
  }
  .canvas { position: relative; width: 1200px; height: 675px; }
  .card {
    position: absolute; left: 415px; top: 35px;
    width: 370px; height: 605px;
    background: linear-gradient(180deg, var(--sky-top) 0%, #d3ecfa 45%, var(--sky-bottom) 100%);
    box-shadow: 0 6px 18px rgba(0,0,0,0.18);
    overflow: hidden;
  }
  .speech-bubble {
    position: absolute; left: 22px; top: 44px;
    width: 326px; height: 200px;
  }
  .speech-bubble svg { position: absolute; inset: 0; }
  .contact {
    position: absolute; left: 0; top: 18px; width: 326px;
    text-align: center; line-height: 1.25;
  }
  .contact-name {
    color: var(--name-red); font-weight: 700; font-size: 30px;
    margin-bottom: 8px;
  }
  .contact-line { font-size: 17px; }
  .contact-phone { color: var(--phone-blue); }
  .contact-email { color: var(--email-white); font-size: 15.5px; }
  .contact-abn { color: var(--abn-yellow); font-weight: 700; margin-top: 4px; }
  .character-art {
    position: absolute; left: 40px; top: 300px;
    width: 290px; height: 165px;
    border-radius: 20px;
    background: linear-gradient(135deg, var(--art-warm) 0%, var(--art-cool) 100%);
    opacity: 0.75;
  }
  .brand {
    position: absolute; left: 0; top: 498px; width: 370px;
    text-align: center;
  }
  .brand-name {
    color: var(--brand-blue); font-weight: 700; font-size: 34px;
    line-height: 1.1;
  }
  .brand-tagline {
    color: var(--tagline-gold); font-size: 14px; letter-spacing: 0.5px;
    margin-top: 10px;
  }
</style>
</head>
<body>
<div class="canvas">
  <div class="card">
    <div class="speech-bubble">
      <svg width="326" height="200" viewBox="0 0 326 200" aria-hidden="true">
        <path d="M40 0 H286 Q326 0 326 40 V120 Q326 160 286 160 H262 L272 200 L226 160 H40 Q0 160 0 120 V40 Q0 0 40 0 Z" fill="var(--bubble)"/>
      </svg>
      <div class="contact">
        <p class="contact-name">Tilda</p>
        <p class="contact-line contact-phone">T: 0498 217 503</p>
        <p class="contact-line contact-email">E: enquiries@brightfoxparties.example.au</p>
        <p class="contact-line contact-abn">ABN: 47 302 658 114</p>
      </div>
    </div>
    <div class="character-art" role="img" aria-label="Illustration of playful party characters: a fairy, a tumbling clown and a pirate"></div>
    <div class="brand">
      <p class="brand-name">Bright Fox</p>
      <p class="brand-tagline">Kids Parties &amp; Events</p>
    </div>
  </div>
</div>
</body>
</html>
```